Webbanner-Design für Ebook - Unterwegs im Süden Ungarns ( Affiliate und Promivo)
Zielgruppe
Wir verkaufen Ebooks. In diesem Fall möchten wir Kroatien Liebhaber aufmerksam machen, dass es mittlerweile ein Buch gibt, welches all die Sehenswürdigkeiten und Routen bis nach Kroatien ausführlich beschreibt.
Aufgabenstellung
Da wir unseren Affiliate Partner die Möglichkeit geben wollen, unsere Produkte zu verkaufen, benötigen wir diesbezüglich gute Anzeigen mit verschiedener Größen. ( affiliate und Promivo )
Sollten Vorlagen / Stockfotos verwendet werden, dann bitte über bildfang
Ich habe einige Fotos welches wir bereits erworben haben hier hochgeladen.
Auch das Coverbild ist im Anhang.
Ideal wäre eine Buch-Abbildung für die Anzeigen.
3 Anzeigegrößen erforderlich
728 x 90 300 x 250 300 x 600

```html
<!DOCTYPE html>
<html lang="de">
<head>
<meta charset="utf-8">
<title>Unterwegs im Süden Ungarns – Banner 300×600</title>
<link rel="stylesheet" href="https://fonts.googleapis.com/css2?family=Roboto+Condensed:wght@300;400;700&family=Zilla+Slab:wght@700&display=swap">
<style>
  :root {
    --bg-top: #ffffff;
    --bg-bottom: #e3e3e3;
    --ink: #1a1a1a;
    --cta: #f26a1b;
    --cta-text: #ffffff;
    --badge-red: #d7141a;
    --badge-ring: #ffffff;
    --swoosh-red: #c8141b;
    --swoosh-blue: #1d4f9c;
    --sky: #cfe3f2;
    --sea-light: #3a8fc4;
    --sea-deep: #0c4f86;
    --coast: #4d6b3a;
  }
  html, body {
    margin: 0;
    padding: 0;
    width: 1200px;
    height: 2400px;
    overflow: hidden;
  }
  .banner {
    position: relative;
    width: 1200px;
    height: 2400px;
    overflow: hidden;
    background: linear-gradient(180deg, var(--bg-top) 0%, var(--bg-bottom) 55%);
    font-family: "Roboto Condensed", "Arial Narrow", sans-serif;
    color: var(--ink);
  }
  .ebook-cover {
    position: absolute;
    left: 690px;
    top: 10px;
    width: 440px;
    height: 340px;
    transform: rotate(-8deg);
    background: #f4f4f4;
    border-radius: 26px;
    box-shadow: 0 18px 40px rgba(0,0,0,0.25);
    padding: 18px;
    box-sizing: border-box;
    z-index: 2;
  }
  .ebook-cover .cover-art {
    width: 100%;
    height: 100%;
    border-radius: 10px;
    background: linear-gradient(160deg, #ffffff 0%, #cfd8e3 35%, #6a8fb3 65%, #2f5c87 100%);
  }
  .headline {
    position: absolute;
    left: 84px;
    top: 300px;
    margin: 0;
    text-transform: uppercase;
    font-weight: 700;
    line-height: 1;
    z-index: 1;
  }
  .headline .small {
    display: block;
    font-weight: 400;
    font-size: 96px;
    line-height: 1.1;
    letter-spacing: 1px;
  }
  .headline .big {
    display: block;
    font-size: 214px;
    line-height: 0.88;
    letter-spacing: -1px;
  }
  .subline {
    position: absolute;
    left: 88px;
    top: 915px;
    margin: 0;
    font-weight: 300;
    font-size: 76px;
    line-height: 1.2;
    text-transform: uppercase;
  }
  .cta {
    position: absolute;
    left: 515px;
    top: 1146px;
    width: 416px;
    height: 112px;
    background: var(--cta);
    color: var(--cta-text);
    font-weight: 700;
    font-size: 50px;
    display: flex;
    align-items: center;
    justify-content: center;
    text-transform: uppercase;
    letter-spacing: 1px;
    z-index: 2;
  }
  .coast-scene {
    position: absolute;
    left: 0;
    top: 0;
    width: 1200px;
    height: 2400px;
  }
  .badge {
    position: absolute;
    left: 515px;
    top: 1290px;
    width: 430px;
    height: 430px;
    border-radius: 50%;
    background: var(--badge-red);
    border: 12px solid var(--badge-ring);
    box-sizing: border-box;
    box-shadow: 0 10px 24px rgba(0,0,0,0.3);
    transform: rotate(-10deg);
    display: flex;
    flex-direction: column;
    align-items: center;
    justify-content: center;
    color: #fff;
    font-family: "Zilla Slab", Georgia, serif;
    text-transform: uppercase;
    z-index: 3;
  }
  .badge .badge-intro {
    font-size: 28px;
    font-weight: 700;
    margin-bottom: 6px;
  }
  .badge ul {
    margin: 0;
    padding: 0;
    list-style: none;
    font-size: 36px;
    font-weight: 700;
    line-height: 1.08;
    letter-spacing: 0.5px;
  }
  .badge li::before {
    content: "•";
    margin-right: 8px;
  }
  .badge li.cont {
    padding-left: 22px;
  }
  .badge li.cont::before { content: none; }
</style>
</head>
<body>
<main class="banner">
  <div class="ebook-cover">
    <div class="cover-art" role="img" aria-label="E-Book-Cover auf einem Tablet: Titel über einer Straße an der Küste"></div>
  </div>

  <h1 class="headline">
    <span class="small">Unterwegs im</span>
    <span class="big">Süden</span>
    <span class="big">Ungarns</span>
  </h1>

  <p class="subline">Der perfekte Guide für<br>Fahrer und Beifahrer</p>

  <svg class="coast-scene" viewBox="0 0 1200 2400">
    <defs>
      <linearGradient id="coast-fill" x1="0" y1="0" x2="0" y2="1">
        <stop offset="0" stop-color="#cfe3f2"/>
        <stop offset="0.22" stop-color="#9fc3dd"/>
        <stop offset="0.38" stop-color="#4d6b3a"/>
        <stop offset="0.6" stop-color="#3a8fc4"/>
        <stop offset="1" stop-color="#0c4f86"/>
      </linearGradient>
    </defs>
    <path d="M0 1372 Q600 1255 1200 1300" fill="none" stroke="#1d4f9c" stroke-width="18"/>
    <path d="M0 1345 Q560 1228 1200 1276" fill="none" stroke="#c8141b" stroke-width="14"/>
    <path role="img" aria-label="Küstenfoto mit Inseln und Meer, davor ein rundes Verkehrsschild mit der Aufschrift Maut" d="M0 1388 Q600 1270 1200 1316 L1200 2400 L0 2400 Z" fill="url(#coast-fill)"/>
  </svg>

  <a class="cta">Mehr erfahren</a>

  <div class="badge">
    <span class="badge-intro">Alles über</span>
    <ul>
      <li>Mautgebühren</li>
      <li>Tunnelgebühren</li>
      <li>Campingplätze</li>
      <li>Sehenswürdig-</li>
      <li class="cont">keiten</li>
    </ul>
  </div>
</main>
</body>
</html>
```